Our Company is Harbourline Lot Partners and we service the whole Perth Metro region. We want our flyer to grab the potential clients attention and inform them of their potential opportunity to subdivide their residential property. We would like the flyer to show our logo, contact details website and maybe one eye catching, engaging picture/photo. If the Flyer could follow the same colours as our logo that would be great. Are we able to have a A5 size flyer front and back? maybe our contact information on the back? and other services that we offer?
A lot of our potential clients aren't aware their house/land is sub dividable, or even know how to do a subdivision. We would like our flyer to educate the average residential home owner of the potential of their property and make the idea of subdividing seem and easy and accessible. Something along the lines of "Looking to Subdivide? Not sure if your property is sub-dividable? Call us now for a obligation free assessment of your property." or maybe "Subdividing you property is easier than you might think..."
We would like to advertise that we offer:-
Free Subdivision feasibility analysis of your property,
Project Management: We offer full Project Management from start to finish ensuring a hassle free subdivision (or something along those lines)-
New title's application
Updates

Target Market(s)

Residential Home owners with the potential to subdivide their property.

Industry/Entity Type

Surveyor

Colors
f78f20
c3c3c3
3176b5

Requirements
Must have
• Simple, clutter free design offering the idea of subdividing as a new, accessible opportunity to the average homeowner.

```html
<!DOCTYPE html>
<html lang="en">
<head>
<meta charset="utf-8">
<title>Harbourline Lot Partners – A5 Flyer Front and Back</title>
<link href="https://fonts.googleapis.com/css2?family=Oswald:wght@500;600&family=Questrial&display=swap" rel="stylesheet">
<style>
  :root{
    --orange:#f0542a;
    --orange-soft:#f78f20;
    --grey:#c3c3c3;
    --blue:#3176b5;
    --ink:#2b2b2b;
    --ink-soft:#3a3a3a;
    --stage:#2a2a2a;
    --paper:#ffffff;
  }
  *{margin:0;padding:0;box-sizing:border-box}
  html,body{width:1200px;height:900px;overflow:hidden}
  body{background:var(--stage);position:relative;font-family:"Questrial",sans-serif}

  .flyer{position:absolute;top:103px;width:490px;height:694px;overflow:hidden;background:var(--paper)}
  .flyer--front{left:72px}
  .flyer--back{left:637px;width:489px}

  .brand{position:absolute;display:flex;align-items:center;gap:8px;color:var(--ink-soft);font-family:"Questrial",sans-serif;font-size:17px;line-height:1.1}
  .brand__dot{width:12px;height:12px;border-radius:50%;background:var(--orange);flex:none}
  .flyer--front .brand{left:28px;top:62px;width:170px;color:#1f2a3a}
  .flyer--back .brand{left:0;right:0;top:50px;justify-content:center}

  /* front */
  .front__photo{position:absolute;inset:0;
    background:linear-gradient(180deg,#3a7fc6 0%,#4f8fd0 22%,#3a5f9a 45%,#1e2a4a 62%,#2a1f2a 72%,#3c4f7a 80%,#6b7fa8 100%)}
  .front__glow{position:absolute;left:0;right:0;top:220px;height:260px;
    background:radial-gradient(ellipse at 40% 70%,rgba(255,190,110,.55),rgba(255,190,110,0) 60%)}

  .headline{position:absolute;left:224px;top:62px;width:240px;font-family:"Oswald",sans-serif;font-weight:600;text-transform:uppercase;color:#fff}
  .headline__ask{display:block;font-size:26px;line-height:30px;letter-spacing:.2px}
  .headline__main{display:flex;align-items:flex-end;gap:8px;margin-top:4px}
  .headline__lead{display:flex;flex-direction:column}
  .headline__big{font-size:54px;line-height:54px;color:var(--orange);letter-spacing:-1px}
  .headline__rule{display:block;height:3px;width:calc(100% + 8px);background:var(--orange);margin-top:2px}
  .headline__stack{display:flex;flex-direction:column;padding-bottom:5px}
  .headline__small{font-size:24px;line-height:24px}
  .headline__area{font-size:44px;line-height:42px;color:var(--orange)}

  .front__curve{position:absolute;left:0;top:0}
  .front__intro{position:absolute;left:20px;right:20px;top:577px;text-align:center;color:#2d2d2d;font-size:17.5px;line-height:24.5px;letter-spacing:.4px}
  .front__footer{position:absolute;left:0;right:0;bottom:0;height:25px;background:rgba(236,236,240,.92);text-align:center;color:var(--orange);font-size:14px;line-height:25px}

  /* back */
  .back__photo{position:absolute;left:0;right:0;top:55px;height:300px;
    background:linear-gradient(180deg,#4f8fd0 0%,#82b2e0 35%,#b8c2c8 60%,#6f8a5a 80%,#4d6b3a 100%)}
  .back__curves{position:absolute;left:0;top:0}
  .offer{position:absolute;left:0;right:0;top:360px;text-align:center;color:var(--ink)}
  .offer__title{font-size:32px;line-height:40px;color:var(--orange);text-transform:uppercase;font-weight:400}
  .offer__list{list-style:none;margin-top:8px;font-size:22px;line-height:27px}
  .offer__list li{margin-bottom:6px}
  .offer__reassure{font-size:33px;line-height:40px;color:var(--orange);margin-top:6px}
  .offer__promise{font-size:20.5px;line-height:25px;text-transform:uppercase;color:#1f1f1f;margin-top:6px}
  .back__rule{position:absolute;left:0;right:0;top:654px;height:3px;background:var(--orange-soft);opacity:.7}
  .back__contact{position:absolute;left:0;right:0;top:657px;bottom:0;background:#cfcfcf;text-align:center;font-size:20px;line-height:37px;color:var(--ink)}
</style>
</head>
<body>

<section class="flyer flyer--front">
  <div class="front__photo" role="img" aria-label="Photo of the Perth city skyline at dusk, lit towers reflected in the river"></div>
  <div class="front__glow"></div>

  <div class="brand"><span class="brand__dot"></span><span>Harbourline Lot Partners</span></div>

  <h1 class="headline">
    <span class="headline__ask">Need subdivisions?</span>
    <span class="headline__main">
      <span class="headline__lead">
        <span class="headline__big">Expats</span>
        <span class="headline__rule"></span>
      </span>
      <span class="headline__stack">
        <span class="headline__small">On your</span>
        <span class="headline__area">Area</span>
      </span>
    </span>
  </h1>

  <svg class="front__curve" width="490" height="694" viewBox="0 0 490 694" aria-hidden="true">
    <path d="M0 566 Q245 478 490 566 L490 694 L0 694 Z" fill="rgba(240,240,244,.78)"/>
    <path d="M0 546 Q245 490 490 546 L490 566 Q245 478 0 566 Z" fill="#ffffff"/>
    <path d="M0 540 Q245 484 490 540" fill="none" stroke="var(--orange)" stroke-width="3"/>
    <polygon points="276,494 279.5,502 288,502 281,507 284,515 276,510 268,515 271,507 264,502 272.5,502" fill="#ffffff"/>
  </svg>

  <p class="front__intro">A Lot Of Our Potential Clients Aren't Aware<br>Their House/land Is Sub Dividable, Or Even<br>Know How To Do A Subdivision.</p>
  <div class="front__footer">www.harbourlinelots.com.au</div>
</section>

<section class="flyer flyer--back">
  <div class="back__photo" role="img" aria-label="Photo of the Perth city skyline by day with parkland in the foreground"></div>

  <svg class="back__curves" width="489" height="694" viewBox="0 0 489 694" aria-hidden="true">
    <path d="M0 0 L489 0 L489 84 Q240 120 0 58 Z" fill="#ffffff"/>
    <path d="M0 58 Q240 120 489 84 L489 92 Q240 132 0 76 Z" fill="var(--orange)"/>
    <path d="M0 312 Q260 270 489 322 L489 694 L0 694 Z" fill="var(--orange)"/>
    <path d="M0 338 Q260 294 489 342 L489 694 L0 694 Z" fill="#f4f4f4"/>
  </svg>

  <div class="brand"><span class="brand__dot"></span><span>Harbourline Lot Partners</span></div>

  <div class="offer">
    <h2 class="offer__title">We Offer</h2>
    <ul class="offer__list">
      <li>Free Land Development Analysis</li>
      <li>Project Management: First time<br>Subdividing?</li>
    </ul>
    <div class="offer__reassure">NO WORRIES!</div>
    <p class="offer__promise">We offer full project management<br>from start to finish<br>ensuring a hassle free subdivision</p>
  </div>

  <div class="back__rule"></div>
  <div class="back__contact">Contact Info</div>
</section>

</body>
</html>
```